Retractable Banner design

We need to a banner design to print on a retractable banner of size 31.5"W X 95.85" H. This banner will be displayed at the universities seminars conducted during campus recruitment process. Audience will be masters gradutes with IT or non-IT background.

Please use images which are suitable for the cause, and also words which emphasize the bright future and jobs. You can come up with suitable colors or using the logo colors. Sample banner, which we used before is attached. Need some attractive designs.

Some of the Text which has to be displaed apart from the images :

For the fresh graduates (OPT/CPT) , Bright Harbor is a learning ground, an opportunity for growth, a stepping stone in the career graph and a substantial elevator for an excellent future.

BENEFITS:

Free Training (CPT / OPT Students) and Free Accomodationm
Project Based Training
Well Experienced faculty working in real time environments
Exposure to Real Time Application, 24/7 access to labs
Free H1-B Processing for eligible OPT students
100% Placement assured
Efficient sales and marketing team, Competetive salary
Zero Cost to you, until you receive your first paycheck

http://www.brightharborvex.com

42 Meadowlark Ave, Ste 610, Piscataway, NJ 08817
Tel: (908)555-0143 Ext : 214

info@brightharborvex.com

Target Market(s)

Masters graduates applying for Jobs

Industry/Entity Type

University

Colors

Designer to choose colors to be used in the design.

```html
<!DOCTYPE html>
<html lang="en">
<head>
<meta charset="utf-8">
<title>Bright Harbor – Retractable Banner</title>
<link href="https://fonts.googleapis.com/css2?family=Montserrat:ital,wght@0,400;0,800;1,800&family=Oswald:wght@300;400&display=swap" rel="stylesheet">
<style>
  :root{
    --canvas:#e9eaeb;
    --white:#ffffff;
    --blue:#1d6fc0;
    --green:#8cc63f;
    --green-soft:#c6e39c;
    --orange:#f39322;
    --dark:#3c3c3c;
    --rule:#6b6b6b;
    --ink-light:#f2f2f2;
  }
  *{margin:0;padding:0;box-sizing:border-box}
  html,body{width:1200px;height:1200px;overflow:hidden;background:var(--canvas)}
  .banner{position:absolute;left:405px;top:10px;width:390px;height:1180px;background:var(--white);box-shadow:0 4px 14px rgba(0,0,0,.18);overflow:hidden;font-family:"Montserrat",sans-serif;color:var(--ink-light)}
  .banner-shapes{position:absolute;inset:0}
  .t{position:absolute}
  .condensed{font-family:"Oswald",sans-serif;font-weight:300;text-transform:uppercase;line-height:1.05;white-space:nowrap}

  .brand{display:flex;align-items:center;gap:7px;font-weight:800;color:var(--blue)}
  .brand-dot{border-radius:50%;background:var(--blue)}
  .brand-top{left:30px;top:52px;font-size:23px}
  .brand-top .brand-dot{width:20px;height:20px}
  .brand-bottom{left:0;width:390px;top:1083px;justify-content:center;font-size:28px}
  .brand-bottom .brand-dot{width:24px;height:24px}

  .placement{left:115px;top:296px;color:var(--white);font-weight:800;font-style:italic;line-height:1}
  .placement .pct{display:block;margin-left:52px;font-size:20px}
  .placement .word{font-style:normal;font-size:15px}
  .placement .word-2{position:relative;top:14px;margin-left:2px}

  .elevator{left:30px;top:545px}
  .elevator .small{font-size:15px;display:block}
  .elevator .big{font-size:21px;display:block;margin-top:2px}
  .intro{left:30px;top:622px;width:152px;font-size:10.3px;line-height:1.4}

  .why-title{left:30px;top:764px;font-size:14px}
  .why-list{left:30px;top:788px;width:142px;list-style:none}
  .why-list li{position:relative;padding-left:11px;font-size:7px;line-height:1.2;padding-bottom:4px;margin-bottom:4px;border-bottom:1px solid var(--rule)}
  .why-list li:last-child{border-bottom:none;margin-bottom:0}
  .why-list svg{position:absolute;left:0;top:1px;width:7px;height:7px}
  .globe{left:78px;top:916px;width:20px;height:20px}
  .web{left:0;width:197px;text-align:center;top:942px;font-family:"Oswald",sans-serif;font-weight:300;font-size:14px}

  .quote{left:227px;top:420px;font-family:"Montserrat",sans-serif;font-weight:800;font-size:80px;color:var(--green-soft);line-height:1}
  .motto{left:227px;top:484px;font-size:19px;color:var(--white)}
  .benefits-title{left:227px;top:566px;display:flex;align-items:center;gap:5px;color:var(--white)}
  .benefits-title .mark{font-size:29px}
  .benefits-title .words{font-size:12.5px;line-height:.95}
  .benefits-list{left:227px;top:628px;width:160px;list-style:none}
  .benefits-list li{position:relative;padding-left:30px;min-height:30px;font-family:"Oswald",sans-serif;font-weight:300;font-size:12.5px;color:var(--white);line-height:1.1}
  .benefits-list li small{display:block;font-size:5.6px;line-height:1.2}
  .benefits-list svg{position:absolute;left:0;top:0;width:18px;height:18px}

  .question{left:228px;top:842px;font-size:17px;color:var(--white)}
  .contact-note{left:228px;top:866px;font-size:5.6px;letter-spacing:.2px;color:var(--white)}
  .phone{left:228px;top:879px;font-size:14px;color:var(--white);display:flex;align-items:center;gap:4px}
  .email{left:228px;top:903px;font-size:8.2px;color:var(--white);display:flex;align-items:center;gap:3px}
  .address{left:228px;top:919px;font-size:7.6px;line-height:1.3;color:var(--white);padding-left:10px}
  .address svg{position:absolute;left:0;top:1px;width:7px;height:9px}
</style>
</head>
<body>
<div class="banner">
  <svg class="banner-shapes" viewBox="0 0 390 1180" width="390" height="1180">
    <defs>
      <linearGradient id="photoTone" x1="0" y1="0" x2="1" y2="1">
        <stop offset="0" stop-color="#8a8d92"/>
        <stop offset=".35" stop-color="#4d6fa8"/>
        <stop offset=".6" stop-color="#b7aaa5"/>
        <stop offset="1" stop-color="#8f9297"/>
      </linearGradient>
    </defs>
    <rect x="0" y="30" width="390" height="560" fill="url(#photoTone)" role="img" aria-label="Photo of a graduate in a grey sweater and blue shirt adjusting his tie"/>
    <path d="M0 250 Q0 210 34 197 L390 52 V66 L38 210 Q10 222 0 262 Z" fill="var(--blue)"/>
    <path d="M0 0 H390 V47 L30 193 Q0 205 0 240 Z" fill="var(--white)"/>
    <path d="M0 532 L390 372 V1050 H0 Z" fill="var(--dark)"/>
    <path d="M197 803 V470 Q197 445 222 434 L390 342 V735 Z" fill="var(--green)"/>
    <path d="M197 1050 V895 Q197 872 222 862 L390 775 V1050 Z" fill="var(--orange)"/>
    <rect x="0" y="1050" width="390" height="105" fill="var(--white)"/>
    <rect x="0" y="1155" width="197" height="25" fill="var(--dark)"/>
    <rect x="197" y="1155" width="193" height="25" fill="var(--orange)"/>
    <line x1="200" y1="322" x2="182" y2="360" stroke="var(--white)" stroke-width="1"/>
    <line x1="30" y1="752" x2="170" y2="752" stroke="var(--rule)"/>
    <line x1="30" y1="904" x2="170" y2="904" stroke="var(--rule)"/>
    <line x1="227" y1="607" x2="278" y2="607" stroke="var(--white)"/>
    <line x1="228" y1="874" x2="330" y2="874" stroke="var(--white)" stroke-width=".6"/>
  </svg>

  <div class="t brand brand-top"><span class="brand-dot"></span>Bright Harbor</div>

  <div class="t placement">
    <span class="pct">100%</span>
    <span class="word">PLACEMENT</span><span class="word word-2">ASSURED</span>
  </div>

  <div class="t elevator condensed">
    <span class="small">Your elevator</span>
    <span class="big">For an excellent<br>future</span>
  </div>
  <p class="t intro">For the fresh graduates (OPT/CPT) , Bright Harbor is a learning ground, an opportunity for growth, a stepping stone in the career graph and a substantial elevator for an excellent future.</p>

  <div class="t why-title condensed">Why with us ?</div>
  <ul class="t why-list">
    <li><svg viewBox="0 0 10 10"><circle cx="5" cy="5" r="5" fill="#fff"/><path d="M2.6 5.2 4.3 6.8 7.5 3.4" stroke="#3c3c3c" stroke-width="1.4" fill="none"/></svg>Free Training (CPT / OPT Students) and Free Accomodation</li>
    <li><svg viewBox="0 0 10 10"><circle cx="5" cy="5" r="5" fill="#fff"/><path d="M2.6 5.2 4.3 6.8 7.5 3.4" stroke="#3c3c3c" stroke-width="1.4" fill="none"/></svg>Well Experienced faculty working in real time environments</li>
    <li><svg viewBox="0 0 10 10"><circle cx="5" cy="5" r="5" fill="#fff"/><path d="M2.6 5.2 4.3 6.8 7.5 3.4" stroke="#3c3c3c" stroke-width="1.4" fill="none"/></svg>Exposure to Real Time Application, 24/7 access to labs</li>
    <li><svg viewBox="0 0 10 10"><circle cx="5" cy="5" r="5" fill="#fff"/><path d="M2.6 5.2 4.3 6.8 7.5 3.4" stroke="#3c3c3c" stroke-width="1.4" fill="none"/></svg>Efficient sales and marketing team, Competetive salary</li>
  </ul>
  <svg class="t globe" viewBox="0 0 20 20" fill="none" stroke="#fff" stroke-width="1.3"><circle cx="10" cy="10" r="8.5"/><ellipse cx="10" cy="10" rx="3.8" ry="8.5"/><path d="M1.5 10h17M3 5.5h14M3 14.5h14"/></svg>
  <div class="t web">www.brightharborvex.com</div>

  <div class="t quote">“</div>
  <div class="t motto condensed">The best way to<br>predict your future<br>is to create it</div>
  <div class="t benefits-title condensed"><span class="mark">BH</span><span class="words">Assured<br>Benefits</span></div>
  <ul class="t benefits-list">
    <li><svg viewBox="0 0 20 20" fill="none" stroke="#fff" stroke-width="1.5"><circle cx="10" cy="10" r="8.5"/><path d="M5.5 10.2 8.6 13.2 15.5 5.5"/></svg>100% Placement assured</li>
    <li><svg viewBox="0 0 20 20" fill="none" stroke="#fff" stroke-width="1.3"><path d="M2 13 17 6 13 14 9 11 5 15 6 11Z"/></svg>Free H1-B Processing<small>for eligible OPT students</small></li>
    <li><svg viewBox="0 0 20 20" fill="none" stroke="#fff" stroke-width="1.3"><circle cx="10" cy="10" r="8.5"/><ellipse cx="10" cy="10" rx="3" ry="4.5"/></svg>Zero Cost to you,<small>until you receive your first paycheck</small></li>
    <li><svg viewBox="0 0 20 20" fill="none" stroke="#fff" stroke-width="1.3"><rect x="2.5" y="3" width="15" height="9"/><path d="M1.5 3h17M6 12l-2 6M14 12l2 6M5 15.5h10"/></svg>Project Based Training</li>
  </ul>

  <div class="t question condensed">Question ?</div>
  <div class="t contact-note">FEEL FREE TO CONTACT US.</div>
  <div class="t phone"><svg width="11" height="11" viewBox="0 0 12 12"><path d="M2.5 1 4.5 1 5.3 3.6 4 4.6C4.8 6.3 5.8 7.3 7.4 8L8.4 6.7 11 7.5V9.6C11 10.4 10.4 11 9.6 11 5 10.7 1.3 7 1 2.4 1 1.6 1.6 1 2.5 1Z" fill="#fff"/></svg>(908)555-0143</div>
  <div class="t email"><svg width="8" height="6" viewBox="0 0 8 6"><rect width="8" height="6" fill="#fff"/><path d="M0 0 4 3.3 8 0" stroke="#f39322" stroke-width=".8" fill="none"/></svg>info@brightharborvex.com</div>
  <div class="t address"><svg viewBox="0 0 7 9" fill="none" stroke="#fff" stroke-width=".8"><path d="M3.5 8.6C1.5 6 .5 4.5 .5 3.3a3 3 0 0 1 6 0C6.5 4.5 5.5 6 3.5 8.6Z"/><circle cx="3.5" cy="3.3" r="1"/></svg>42 Meadowlark Ave,<br>Ste 610, Piscataway, NJ 08817<br>Tel: (908)555-0143 Ext : 214</div>

  <div class="t brand brand-bottom"><span class="brand-dot"></span>Bright Harbor</div>
</div>
</body>
</html>
```